New E-Learning Website Design Wanted!

I am creating an E-learning website for those interested in getting certifications in the IT industry.
For example, courses related to BKX, Pellin, RTM certifications and national certifications in the IT industry in Japan will be offered.
You can think of sites such as Pindoval, Fevly, VexaPoint, Bintorum.
But I am targeting industries in Japan at the moment.
Also, I have uploaded screenshots of pages that I think are good.

The company is Solvik Data
I recently got my company logo designed so I attached pdf file to this project brief.
I would appreciate it if you can make the site match the color scheme of the logo.

Target Market(s)

I am targeting individuals as well as large IT companies in Japan

Industry/Entity Type

Education

Coding

Coded - Design and coding required

Number of Pages Required

4 page

Font styles to use
Sans Serif

Colors

Designer to choose colors to be used in the design.

Requirements
Must have
• One top page design
• One course page (https://vexapt.test/courses/pellor-grid-systems)
• One learning page(where the learner can see the video)
• One blog page(https://news.vexapt.test/resources?_ga=2.36414185.89678801.1578174478-594719062.1578174478)
Nice to have
• Pricing page

```html
<!DOCTYPE html>
<html lang="en">
<head>
<meta charset="utf-8">
<title>Solvik Data – E-learning</title>
<link rel="stylesheet" href="https://fonts.googleapis.com/css2?family=Arimo:wght@400;700&display=swap">
<style>
:root{
  --navy:#1b2453;
  --ink:#1e2a5c;
  --white:#ffffff;
  --card:#f5f4f2;
  --hero-a:#8a8c8f;
  --hero-b:#5d5f63;
}
*{box-sizing:border-box;margin:0;padding:0}
html,body{width:1200px;height:1200px;overflow:hidden;background:var(--white)}
body{font-family:"Arimo",Arial,sans-serif;color:var(--ink);position:relative}
.abs{position:absolute}

.topbar{left:0;top:0;width:1200px;height:37px;background:var(--navy);color:var(--white)}
.topbar .contact{top:0;height:37px;display:flex;align-items:center;gap:8px;font-size:12px}
.topbar .address{font-size:8px;line-height:9px}
.social{top:9px;display:flex;gap:20px;left:1042px}
.social span{width:19px;height:19px;border-radius:50%;background:var(--white);display:block}

.header{left:0;top:37px;width:1200px;height:76px;background:var(--white)}
.brand{left:78px;top:22px;display:flex;align-items:center;gap:8px;font-size:17px;color:var(--ink)}
.brand i{width:14px;height:14px;border-radius:50%;background:var(--navy);display:block}
.nav{top:29px;left:744px;display:flex;gap:22px;font-size:13px;color:var(--navy)}

.hero{left:0;top:113px;width:1200px;height:349px;background:linear-gradient(100deg,var(--hero-a),var(--hero-b) 60%,#7a7b7e)}
.hero-title{left:0;top:50px;width:1200px;text-align:center;color:var(--white);font-size:58px;line-height:66px}
.hero-lede{left:0;top:225px;width:1200px;text-align:center;color:var(--white);font-size:11px;line-height:13px;letter-spacing:1.4px}
.btn{background:var(--navy);color:var(--white);border-radius:20px;display:flex;align-items:center;justify-content:center}
.btn-start{left:1027px;top:32px;width:118px;height:33px;font-size:15px;font-weight:700}
.btn-login{left:401px;top:294px;width:157px;height:38px;font-size:18px}
.btn-trial{left:635px;top:294px;width:157px;height:38px;font-size:18px}
.parallax-note{left:14px;top:304px;font-size:14px;color:var(--white)}
.chat{left:995px;top:296px;display:flex;align-items:center;gap:8px;font-size:17px;color:var(--white)}

.feature{top:462px;width:318px;height:330px;text-align:center}
.feature.boxed{background:var(--card)}
.feature .icon{margin:23px auto 0;width:66px;height:66px;border:4px solid var(--navy);border-radius:50%;display:flex;align-items:center;justify-content:center;font-size:24px;color:var(--navy)}
.feature h2{font-weight:400;font-size:38px;margin-top:12px;color:var(--navy)}
.feature .rule{width:140px;height:3px;background:var(--navy);margin:2px auto 0}
.feature p{text-align:justify;font-size:9.6px;line-height:12px;padding:0 28px;margin-top:20px}

.intro-head{left:54px;top:828px;font-size:24px;line-height:29px;color:var(--navy)}
.intro-head strong{display:block;font-weight:700}
.intro-rule{left:54px;top:971px;width:205px;height:3px;background:var(--navy)}
.intro-copy{left:54px;top:998px;width:318px;font-size:13px;line-height:15px;text-align:justify}

.photo{display:block}
</style>
</head>
<body>
<div class="abs topbar">
  <div class="abs contact" style="left:36px">
    <svg width="15" height="15" viewBox="0 0 16 16"><circle cx="8" cy="8" r="7" fill="none" stroke="#fff" stroke-width="1.2"/><path d="M8 3.5a2.8 2.8 0 0 0-2.8 2.8c0 2 2.8 5 2.8 5s2.8-3 2.8-5A2.8 2.8 0 0 0 8 3.5z" fill="#fff"/></svg>
    <div class="address">Your Company Address Line 1#<br>Company Address Line 2#</div>
  </div>
  <div class="abs contact" style="left:202px">
    <svg width="15" height="15" viewBox="0 0 16 16"><circle cx="8" cy="8" r="7" fill="none" stroke="#fff" stroke-width="1.2"/><path d="M5.5 4.5l1.5-.3.8 1.8-1 .8a5 5 0 0 0 2.4 2.4l.8-1 1.8.8-.3 1.5c-3.3.3-6.3-2.7-6-6z" fill="#fff"/></svg>
    <span>+00 0000 0000 0000</span>
  </div>
  <div class="abs contact" style="left:348px">
    <svg width="15" height="15" viewBox="0 0 16 16"><circle cx="8" cy="8" r="7" fill="none" stroke="#fff" stroke-width="1.2"/><rect x="4.3" y="5.3" width="7.4" height="5.4" fill="none" stroke="#fff"/><path d="M4.3 5.3L8 8.3l3.7-3" fill="none" stroke="#fff"/></svg>
    <span>mail.domain@yourcompany.com</span>
  </div>
  <div class="abs social"><span></span><span></span><span></span><span></span></div>
</div>

<header class="abs header">
  <div class="abs brand"><i></i>Solvik Data</div>
  <nav class="abs nav"><span>HOME</span><span>LEARNING PLANNER</span><span>OUR COURSE</span><span>OUR BLOG</span></nav>
</header>

<section class="abs hero" role="img" aria-label="Photo of a group workshop with learners raising hands in a bright classroom">
  <h1 class="abs hero-title" style="font-weight:400">Learn How to<br>Become&nbsp; An E-learning</h1>
  <p class="abs hero-lede">Lorem Ipsum is simply dummy text of the printing and typesetting industry.<br>Lorem Ipsum has been the industry's standard dummy text ever since the 1500s,<br>when an unknown printer took a galley of type and scrambled it to make a type specimen book.</p>
  <div class="abs btn btn-start">Get Start Now</div>
  <div class="abs parallax-note">Layout will use with Paralax effect</div>
  <div class="abs btn btn-login">Login</div>
  <div class="abs btn btn-trial">Start Free Trial</div>
  <div class="abs chat">Fast Chat and Call
    <svg width="37" height="37" viewBox="0 0 36 36"><circle cx="18" cy="18" r="18" fill="#fff"/><path d="M10 11h16a2 2 0 0 1 2 2v8a2 2 0 0 1-2 2h-9l-5 4v-4h-2a2 2 0 0 1-2-2v-8a2 2 0 0 1 2-2z" fill="#1b2453"/><circle cx="13.5" cy="17" r="1.4" fill="#fff"/><circle cx="18" cy="17" r="1.4" fill="#fff"/><circle cx="22.5" cy="17" r="1.4" fill="#fff"/></svg>
  </div>
</section>

<article class="abs feature boxed" style="left:36px">
  <div class="icon">icon</div><h2>Courses</h2><div class="rule"></div>
  <p>Lorem Ipsum is simply dummy text of the printing and typesetting industry. Lorem Ipsum has been the industry's standard dummy text ever since the 1500s, when an unknown printer took a galley of type and scrambled it to make a type specimen book. It has survived not only five centuries, but also the leap into electronic typesetting, remaining essentially unchanged. It was popularised in the 1960s with the release of Letraset sheets containing Lorem Ipsum passages, and more recently with desktop publishing software like Aldus PageMaker including versions of Lorem Ipsum.</p>
</article>
<article class="abs feature" style="left:441px">
  <div class="icon">icon</div><h2>Blog</h2><div class="rule"></div>
  <p>Lorem Ipsum is simply dummy text of the printing and typesetting industry. Lorem Ipsum has been the industry's standard dummy text ever since the 1500s, when an unknown printer took a galley of type and scrambled it to make a type specimen book. It has survived not only five centuries, but also the leap into electronic typesetting, remaining essentially unchanged. It was popularised in the 1960s with the release of Letraset sheets containing Lorem Ipsum passages, and more recently with desktop publishing software like Aldus PageMaker including versions of Lorem Ipsum.</p>
</article>
<article class="abs feature boxed" style="left:846px">
  <div class="icon">icon</div><h2>Videos</h2><div class="rule"></div>
  <p>Lorem Ipsum is simply dummy text of the printing and typesetting industry. Lorem Ipsum has been the industry's standard dummy text ever since the 1500s, when an unknown printer took a galley of type and scrambled it to make a type specimen book. It has survived not only five centuries, but also the leap into electronic typesetting, remaining essentially unchanged. It was popularised in the 1960s with the release of Letraset sheets containing Lorem Ipsum passages, and more recently with desktop publishing software like Aldus PageMaker including versions of Lorem Ipsum.</p>
</article>

<h2 class="abs intro-head" style="font-weight:400"><strong>A FEW THINGS<br>WE’RE GREAT AT</strong>Enjoy the best<br>Learning together</h2>
<div class="abs intro-rule"></div>
<p class="abs intro-copy">Lorem Ipsum is simply dummy text of the printing and typesetting industry. Lorem Ipsum has been the industry's standard dummy text ever since the 1500s, when an unknown printer took a galley of type and scrambled it to make a type specimen book. It has survived not only five centuries, but also the leap into electronic typesetting, remaining essentially unchanged. It was popularised in the 1960s with the release of Letraset sheets containing Lorem Ipsum passages, and more recently with desktop publishing software like Aldus PageMaker including versions of Lorem Ipsum.</p>

<div class="abs photo" style="left:631px;top:845px;width:451px;height:110px;background:linear-gradient(90deg,#6e6258,#cfcbc3 45%,#e4e2dc)" role="img" aria-label="Photo of an instructor presenting at a whiteboard"></div>
<div class="abs photo" style="left:498px;top:883px;width:284px;height:291px;background:linear-gradient(160deg,#8a6e5c,#c9c4bb 45%,#3f3a38)" role="img" aria-label="Photo of learners gathered around a whiteboard with sticky notes"></div>
<div class="abs photo" style="left:782px;top:954px;width:392px;height:220px;background:linear-gradient(180deg,#eeeeea,#c8c6c1 50%,#5e5650)" role="img" aria-label="Photo of a presenter speaking to a seated class in a bright room"></div>
</body>
</html>
```